Law Firm Header Revision

Task: Redesign my law firm Word document header (modern, succinct, logo-first, easy address updates)

I need you to revise and modernize my Microsoft Word document header for Law Office of Bryce Holloman, PLLC. The result should look professional and clean on letters (including Letters of Protection), with the logo as the main focus and the text kept succinct.

Goals:
1. Create a modern, minimal header that feels premium and uncluttered.
Make the logo the most visually dominant element.
Reduce the visual weight of the contact/address block so it doesn’t distract from the document.
Make the address easy to change later (I’m moving offices soon) while keeping the same header design.

2. Content to include (keep all info accurate):
Law Office of Bryce Holloman, PLLC
615 Marrowfield Ave. Ste #300-214, Houston, TX 77019
Office: 832.555.0143
Direct: 713.555.0186
Fax: 832.555.0127
Bhollomanlaw.com

3. Layout requirements:
Provide 3 header style options:
Logo left + contact info right
Centered logo + single concise contact line below
Logo left + firm name prominent + minimal contact line
The primary line near the logo should be minimal (preferably website + main office phone).
The address should be easy to update in one place without redesigning the header. Prefer either:
Move the full address to the footer, or
Put the address in a single dedicated line/block so I can edit it once and keep the layout unchanged.
4. Build constraints:
Must be achievable using standard Microsoft Word tools only (header/footer, tables, alignment, fonts, spacing). No advanced graphics software.
Provide exact header text, plus step-by-step Word instructions for each option:
Font recommendations + sizes
Alignment
Spacing
Table setup (if used)
How to keep it consistent across pages

5. Deliverable:
For each of the 3 options, provide:
The exact header content (with line breaks)
Formatting specs (fonts, sizes, spacing)
Word build steps so I can recreate it reliably and keep the logo as the focal point.

```html
<!DOCTYPE html>
<html lang="en">
<head>
<meta charset="utf-8">
<title>Law Office of Bryce Holloman, PLLC – Letterhead</title>
<link rel="stylesheet" href="https://fonts.googleapis.com/css2?family=Oranienbaum&family=Poppins:wght@400;600&display=swap">
<style>
  :root {
    --navy: #0f1e33;
    --navy-2: #1b3150;
    --navy-3: #27476c;
    --blue: #2d5f95;
    --paper: #ffffff;
    --backdrop: #6b6b6b;
    --ink: #1a1a1a;
  }
  * { margin: 0; padding: 0; box-sizing: border-box; }
  html, body {
    width: 1200px; height: 800px; overflow: hidden;
    background: var(--backdrop);
  }
  .letterhead {
    position: absolute;
    left: 332px; top: 20px;
    width: 537px; height: 760px;
    background: var(--paper);
    box-shadow: 0 4px 18px rgba(0,0,0,.25);
  }
  .brand {
    position: absolute; left: 41px; top: 44px;
    display: flex; align-items: center; gap: 10px;
    height: 53px;
  }
  .brand-square {
    width: 53px; height: 53px; background: var(--navy);
    flex: none;
  }
  .brand-name {
    font-family: "Oranienbaum", serif;
    font-size: 30px; line-height: 1;
    color: var(--navy);
    white-space: nowrap;
  }
  .contact-box {
    position: absolute; left: 335px; top: 41px;
    width: 202px; height: 59px;
    background: var(--navy);
    color: #fff;
    font-family: "Poppins", sans-serif;
    font-size: 10px; line-height: 13.4px;
    padding: 10px 0 0 30px;
  }
  .contact-box strong, .address-bar strong { font-weight: 600; }
  .address-bar {
    position: absolute; left: 0; top: 118px;
    width: 100%; height: 15px;
    background: var(--navy);
    color: #fff;
    font-family: "Poppins", sans-serif;
    font-size: 10.4px; line-height: 15px;
    padding-left: 46px;
    white-space: nowrap;
  }
  .doc-title {
    position: absolute; left: 41px; top: 689px;
    font-family: "Oranienbaum", serif;
    font-size: 17px; color: var(--ink);
  }
  .page-number {
    position: absolute; right: 49px; top: 697px;
    font-family: "Oranienbaum", serif;
    font-size: 10.5px; color: var(--ink);
  }
  .footer-stripe {
    position: absolute; left: 0; top: 715px;
    width: 100%; height: 14.5px;
    display: flex;
  }
  .footer-stripe span { flex: 1; }
  .footer-stripe .s1 { background: var(--navy); }
  .footer-stripe .s2 { background: var(--navy-2); }
  .footer-stripe .s3 { background: var(--navy-3); }
  .footer-stripe .s4 { background: var(--blue); }
  .website {
    position: absolute; left: 0; top: 733px; width: 100%;
    text-align: center;
    font-family: "Poppins", sans-serif;
    font-size: 10px; letter-spacing: 1.3px;
    color: var(--ink);
  }
</style>
</head>
<body>
  <main class="letterhead">
    <header>
      <div class="brand">
        <div class="brand-square"></div>
        <div class="brand-name">BRYCE HOLLOMAN</div>
      </div>
      <div class="contact-box">
        <div><strong>Office:</strong> 832-555-0143</div>
        <div><strong>Direct:</strong> 713-555-0186</div>
        <div><strong>Fax:</strong> 832-555-0127</div>
      </div>
      <div class="address-bar"><strong>Law Office of Bryce Holloman, PLLC,</strong> 615 Marrowfield Ave. Ste #300-214, Houston, TX 77019</div>
    </header>
    <footer>
      <div class="doc-title">Letter of Protection</div>
      <div class="page-number">Page 1</div>
      <div class="footer-stripe"><span class="s1"></span><span class="s2"></span><span class="s3"></span><span class="s4"></span></div>
      <div class="website">www.bhollomanlaw.com</div>
    </footer>
  </main>
</body>
</html>
```